Plate Bright Class (workshop to teach people to eat fruits and vegetables)

Double sided DL Flyer

Free Community Workshop
Plate Bright Live Light
Central Coast NSW

Copy to appear on flyer side one:-
PLATE BRIGHT LIVE LIGHT
interactive workshops
March-April 2019
Presented by qualified nutritionist

Food for healthier happier life for you and your family (free to central coast residents - all ages welcome

Side 2
Learn About:-
Foods that improve your health
basic nutrition
gut brain connection
portion size
menu planning
preparation
eating

Benefits
Improved health
Improved Energy
Manage chronic illness
diabetes type II
cholesterol
Blood Pressure
Family fun

Food Tastings
Lucky Door Prize

Reserve for spot online @ www.platebright.com.au or call 0482 916 304
Supported by Harbourview Shire Council (Logo) Tidewater Rovers Club (Logo) Pinebrook Veterans Club (Logo)

I would like to see a flyer that is bright, fun and fresh with images of fresh food.

Target Market(s)

Women 30 plus

Industry/Entity Type

Health And Wellness

Logo Text

PLATE BRIGHT LIVE LIGHT

Font styles to use
Other font styles liked:
• bold clean

Colors
f37122
9bcb3c
fbed22
ec1f27
e34297

Requirements
Must have
• bright eye catching colours featuring fresh fruit and vegetables
• I have attached a some images of designs I like
Nice to have
• Im happy for the designer to change copy to create a clean flyer without loosing essential information
• I like the feel of the banner on my facebook page
• Sunroot Kitchen - Plate Bright Live Light with Delia Frome
• https://www.facebook.com/sunrootkitchenoz/
Should not have
• old fashioned images

```html
<!DOCTYPE html>
<html lang="en">
<head>
<meta charset="utf-8">
<title>Plate Bright Class – Flyer Side 2</title>
<link rel="stylesheet" href="https://fonts.googleapis.com/css2?family=Arimo:wght@400;700&display=swap">
<style>
  :root {
    --orange: #f37122;
    --green: #9bcb3c;
    --yellow: #fbed22;
    --red: #ec1f27;
    --pink: #e34297;
    --ink: #111111;
    --grey: #333333;
    --navy: #1d3f7a;
    --white: #ffffff;
    --paper: #ffffff;
  }
  * { box-sizing: border-box; margin: 0; padding: 0; }
  html, body { width: 1200px; height: 630px; overflow: hidden; background: var(--paper); }
  body { font-family: "Arimo", Arial, sans-serif; color: var(--ink); }

  .flyer { position: relative; width: 1200px; height: 630px; background: var(--paper); overflow: hidden; }

  .trim-line {
    position: absolute; left: 60px; top: 60px; width: 1080px; height: 510px;
    border: 2px dashed var(--ink); z-index: 6; pointer-events: none;
  }

  .learn-panel {
    position: absolute; left: 100px; top: 60px; width: 360px; height: 442px;
    background: var(--orange); border-bottom-left-radius: 62px; z-index: 1;
  }
  .benefits-panel {
    position: absolute; left: 483px; top: 100px; width: 357px; height: 470px;
    background: var(--green); border-top-left-radius: 62px; z-index: 1;
  }

  .photo-carrots {
    position: absolute; left: 212px; top: 232px; width: 262px; height: 338px;
    background: linear-gradient(160deg, #5f9a35 0%, #7fb046 35%, #f08a2c 60%, #e2611a 100%);
    border-radius: 40px 80px 0 0; opacity: 0.85; z-index: 2;
  }
  .photo-apples {
    position: absolute; left: 672px; top: 300px; width: 258px; height: 270px;
    background: radial-gradient(circle at 45% 40%, #c7e27a 0%, #9cc64a 50%, #6f9b2c 100%);
    border-radius: 48% 48% 10px 10px; opacity: 0.9; z-index: 2;
  }

  .panel-heading {
    position: absolute; color: var(--white); font-weight: 700; font-size: 41px; z-index: 4;
  }
  .learn-heading { left: 139px; top: 102px; }
  .benefits-heading { left: 520px; top: 155px; }

  .bullet-list {
    position: absolute; list-style: none; color: var(--white);
    font-weight: 700; font-size: 23px; line-height: 38px; z-index: 4;
  }
  .bullet-list li { position: relative; padding-left: 21px; }
  .bullet-list li::before {
    content: ""; position: absolute; left: 1px; top: 16px; width: 7px; height: 7px;
    border-radius: 50%; background: var(--white);
  }
  .bullet-list .sub-list { list-style: none; line-height: 33px; }
  .bullet-list .sub-list li { padding-left: 20px; }
  .bullet-list .sub-list li::before {
    top: 13px; width: 8px; height: 8px; background: none; border: 2px solid var(--white);
  }
  .bullet-list .tight { line-height: 31px; }
  .learn-list { left: 139px; top: 172px; width: 310px; }
  .learn-list li.wrap { line-height: 30px; margin-bottom: 7px; margin-top: 4px; }
  .benefits-list { left: 520px; top: 214px; width: 300px; }
  .benefits-list .gap-top { margin-top: 4px; }

  .badge {
    position: absolute; border-radius: 50%; display: flex; flex-direction: column;
    align-items: center; justify-content: center; text-align: center; font-weight: 700; z-index: 5;
  }
  .badge-prize { left: 740px; top: 66px; width: 144px; height: 144px; background: var(--red); color: var(--white); }
  .badge-prize .big { font-size: 24px; line-height: 26px; }
  .badge-prize .small { font-size: 16px; }
  .badge-tastings { left: 867px; top: 89px; width: 102px; height: 102px; background: var(--yellow); color: var(--ink); font-size: 16px; line-height: 20px; }

  .brand {
    position: absolute; left: 1000px; top: 92px; width: 110px; text-align: center; z-index: 5;
    display: flex; flex-direction: column; align-items: center; gap: 6px;
  }
  .brand-dot { width: 30px; height: 30px; border-radius: 50%; background: var(--red); }
  .brand-name { color: var(--green); font-weight: 700; font-size: 17px; line-height: 19px; }

  .booking {
    position: absolute; left: 860px; top: 207px; width: 260px; text-align: center; z-index: 5;
  }
  .booking-line { font-size: 18px; color: var(--grey); line-height: 22px; }
  .booking-web { font-size: 18px; font-weight: 700; color: var(--pink); line-height: 24px; }
  .booking-phone { font-size: 31px; font-weight: 700; color: var(--ink); margin-top: 10px; letter-spacing: 0.5px; }

  .supporters-label { position: absolute; left: 982px; top: 362px; font-size: 18px; color: var(--grey); z-index: 5; }
  .supporter {
    position: absolute; display: flex; align-items: center; gap: 7px; z-index: 5;
    color: var(--navy); font-weight: 700; font-size: 14px; line-height: 16px;
  }
  .supporter-mark { flex: none; width: 26px; height: 26px; border-radius: 50%; background: var(--navy); }
  .supporter-council { left: 940px; top: 400px; width: 190px; }
  .supporter-veterans { left: 940px; top: 442px; width: 190px; }
  .supporter-rovers { left: 940px; top: 496px; width: 190px; font-size: 17px; }
</style>
</head>
<body>
<main class="flyer">
  <div class="learn-panel"></div>
  <div class="benefits-panel"></div>

  <div class="photo-carrots" role="img" aria-label="Photo of a bunch of fresh carrots with green tops"></div>
  <div class="photo-apples" role="img" aria-label="Photo of stacked green apples with one cut in half"></div>

  <h2 class="panel-heading learn-heading">Learn About:</h2>
  <ul class="bullet-list learn-list">
    <li class="wrap">Foods that improve your health</li>
    <li>Basic nutrition</li>
    <li>Gut brain connection</li>
    <li>Portion size</li>
    <li>Menu planning</li>
    <li>Preparation</li>
    <li>Eating</li>
  </ul>

  <h2 class="panel-heading benefits-heading">Benefits:</h2>
  <ul class="bullet-list benefits-list">
    <li>Improved Health</li>
    <li>Improved Energy</li>
    <li class="tight">Manage Chronic Illness
      <ul class="sub-list">
        <li>Diabetes Type II</li>
        <li>Cholesterol</li>
        <li>Blood Pressure</li>
      </ul>
    </li>
    <li class="gap-top">Family fun</li>
  </ul>

  <div class="badge badge-prize"><span class="big">LUCKY</span><span class="small">Door Prize</span></div>
  <div class="badge badge-tastings">Food<br>Tastings</div>

  <div class="brand">
    <span class="brand-dot"></span>
    <span class="brand-name">Sunroot Kitchen</span>
  </div>

  <div class="booking">
    <p class="booking-line">Reserve for spot online</p>
    <p class="booking-web">www.platebright.com.au</p>
    <p class="booking-line">or call</p>
    <p class="booking-phone">0482 916 304</p>
  </div>

  <p class="supporters-label">Supported by:</p>
  <div class="supporter supporter-council"><span class="supporter-mark"></span>Harbourview Shire Council</div>
  <div class="supporter supporter-veterans"><span class="supporter-mark"></span>Pinebrook Veterans Club</div>
  <div class="supporter supporter-rovers"><span class="supporter-mark"></span>Tidewater Rovers Club</div>

  <div class="trim-line"></div>
</main>
</body>
</html>
```